New profile page for existing party website

For the party website 'Revelmap' we need a new design for the user profile page.

The page should show
* a profile picture
* basic information like name, age and city
* music styles he/she likes
* links to their Chatterly profile and website
* a bio (HTML content)
* events they plan to go to
* past events
* pictures

Challenge is that some users may have little information (just their name) while others have a huge description, lots of foto's, events, etc.

Please visit http://www.revelmap.example and http://www.revelmap.example/users/gordon

Target Market(s)

Men and women between 18 and 35

Industry/Entity Type

Night Club

Number of Pages Required

2 page

Font styles to use
Other font styles liked:
• Roboto

Requirements
Must have
• Please design how the page looks with a fully filled out profile and with an empty profile.
• It should fit well with the existing website.
• Include designs for both for small screens (mobile) and large screens (tablet, desktop).
Nice to have
• UX design on how to collapse or paginate sections.
• Interactive effects would be a bonus.
Should not have
• The page should not have subnavigation like menus or tabs.

```html
<!DOCTYPE html>
<html lang="nl">
<head>
<meta charset="utf-8">
<title>Revelmap – Profiel</title>
<link href="https://fonts.googleapis.com/css2?family=Roboto:wght@400;500;700&display=swap" rel="stylesheet">
<style>
:root{
  --ink:#0b0b0b;
  --sidebar:#141414;
  --panel:#1b1b1b;
  --panel-head:#262626;
  --line:#3a3a3a;
  --paper:#ffffff;
  --text:#ffffff;
  --muted:#c9c9c9;
  --accent:#f0f0f0;
  --poster-green:#2f8f3c;
  --poster-teal:#bfe2da;
  --poster-cream:#f2ede3;
  --poster-navy:#1f2b37;
  --photo-a:#d98a3a;
  --photo-b:#8a5a3a;
  --photo-c:#c9a27a;
  --photo-d:#6d8a4a;
}
*{box-sizing:border-box;margin:0;padding:0}
html,body{width:1200px;height:4592px;overflow:hidden}
body{background:var(--paper);font-family:'Roboto',sans-serif;color:var(--text);position:relative}

.topbar{position:absolute;left:0;top:0;width:1200px;height:40px;background:var(--ink);display:flex;align-items:center}
.brand{position:absolute;left:28px;top:7px;font-size:21px;font-weight:700;color:var(--text);letter-spacing:.5px}
.main-nav{position:absolute;left:488px;top:0;height:40px;display:flex;align-items:center;gap:16px;font-size:13px;color:var(--muted)}
.search{position:absolute;left:806px;top:10px;width:118px;height:22px;background:#fff;border-radius:2px;font-size:11px;color:#888;padding:4px 6px}
.account{position:absolute;left:950px;top:6px;display:flex;align-items:center;gap:8px;font-size:13px;color:var(--muted)}
.account .avatar-mini{width:28px;height:28px;background:#8a5a3a;border-radius:2px}

.sidebar{position:absolute;left:0;top:40px;width:290px;height:4465px;background:var(--sidebar);text-align:center}
.profile-photo{position:absolute;left:47px;top:85px;width:200px;height:200px;border-radius:50%;background:radial-gradient(circle at 50% 40%,#c98a4a,#5a3a28 70%);border:4px solid #2a2a2a}
.profile-name{position:absolute;left:0;top:300px;width:290px;font-size:30px;font-weight:400}
.profile-meta{position:absolute;left:0;top:362px;width:290px;font-size:15px;font-weight:700;line-height:23px}
.profile-links{position:absolute;left:76px;top:494px;display:flex;gap:14px}
.profile-links svg{width:26px;height:26px}
.sidebar-rule{position:absolute;left:0;top:2280px;width:290px;height:1px;background:#2c2c2c}

.message-btn{position:absolute;left:1110px;top:66px;width:78px;height:28px;background:var(--panel);color:var(--text);font-size:12px;border-radius:3px;text-align:center;line-height:28px}

.section{position:absolute;left:318px;width:863px}
.section-head{height:36px;display:flex;align-items:center;justify-content:space-between;padding:0 12px;font-size:17px;font-weight:700}
.section-head svg{width:22px;height:14px}
.head-light{background:var(--accent);color:var(--ink)}
.head-dark{background:var(--panel-head);color:var(--text)}
.section-body{background:var(--panel)}

.bio{top:110px}
.bio .section-body{height:742px;padding:22px 14px;font-size:13.4px;line-height:1.45}
.bio h3{font-size:15px;font-weight:700;margin-bottom:16px}
.bio p{margin-bottom:15px}
.bio b{font-weight:700}

.planned{top:905px}
.past{top:2222px}
.event-list{list-style:none}
.event{height:213px;position:relative;border-bottom:1px solid var(--line)}
.event:last-child{border-bottom:none}
.poster{position:absolute;left:19px;top:36px;width:320px;height:140px}
.poster .date{position:absolute;right:8px;top:6px;font-size:12px;font-weight:700;color:var(--ink);background:rgba(255,255,255,.9);padding:2px 6px}
.p-green{background:linear-gradient(135deg,#1f6b2a,var(--poster-green) 60%,#b3d437)}
.p-teal{background:linear-gradient(135deg,var(--poster-teal),#e6f3ef)}
.p-cream{background:linear-gradient(135deg,var(--poster-cream),#f7d7c4 50%,#cfe6ef)}
.p-navy{background:var(--poster-navy)}
.event-info{position:absolute;left:362px;top:34px;font-size:13px;line-height:22px}
.event-info h4{font-size:14px;font-weight:700;margin-bottom:4px}
.event-info li{list-style:none;display:flex;align-items:center;gap:8px;font-weight:500}
.event-info svg{width:13px;height:13px;flex:none}

.photos{top:3538px}
.photo-grid{display:grid;grid-template-columns:repeat(5,1fr);grid-template-rows:repeat(4,146px);gap:4px;margin-top:6px}
.photo{background:var(--photo-a)}
.photo.big{grid-column:span 2;grid-row:span 2}
.photo:nth-child(3n){background:var(--photo-b)}
.photo:nth-child(4n){background:var(--photo-c)}
.photo:nth-child(5n){background:var(--photo-d)}

.footer{position:absolute;left:0;top:4505px;width:1200px;height:87px;background:var(--ink);text-align:center}
.footer-links{padding-top:28px;font-size:12px;font-weight:700;letter-spacing:.3px}
.footer-links span{color:var(--muted);margin:0 8px}
.copyright{font-size:10px;color:#888;margin-top:8px}
</style>
</head>
<body>

<header class="topbar">
  <div class="brand">Revelmap</div>
  <nav class="main-nav"><span>Home</span><span>Agenda</span><span>Vrijkaarten</span><span>Foto's</span><span>Nieuws</span></nav>
  <div class="search">Zoeken</div>
  <div class="account"><div class="avatar-mini" role="img" aria-label="Profielfoto gebruiker"></div>Gordon Vale ▾</div>
</header>

<aside class="sidebar">
  <div class="profile-photo" role="img" aria-label="Profielfoto van de fotograaf"></div>
  <div class="profile-name">MikeyR Photography</div>
  <div class="profile-meta">
    Member since - January 1, 2006<br>
    Age - 34<br>
    City - Amsterdam,<br>
    Music - Latin / Salsa
  </div>
  <div class="profile-links">
    <svg viewBox="0 0 26 26" aria-label="Chatterly"><rect x="2" y="2" width="22" height="22" rx="3" fill="#e0e0e0"/></svg>
    <svg viewBox="0 0 26 26" aria-label="Website"><rect x="2" y="2" width="22" height="22" rx="3" fill="#e0e0e0"/><circle cx="13" cy="13" r="6" fill="none" stroke="#141414" stroke-width="2"/></svg>
    <svg viewBox="0 0 26 26" aria-label="Profiel"><rect x="2" y="2" width="22" height="22" rx="3" fill="#e0e0e0"/></svg>
    <svg viewBox="0 0 26 26" aria-label="E-mail"><rect x="2" y="5" width="22" height="16" rx="2" fill="#e0e0e0"/><path d="M3 6l10 8 10-8" fill="none" stroke="#141414" stroke-width="2"/></svg>
  </div>
  <div class="sidebar-rule"></div>
</aside>

<div class="message-btn">Message</div>

<section class="section bio">
  <div class="section-head head-light">Biography<svg viewBox="0 0 22 14"><path d="M2 2l9 9 9-9" fill="none" stroke="#0b0b0b" stroke-width="4"/></svg></div>
  <div class="section-body">
    <h3>MikeyR Photography</h3>
    <p><b>Function : Head promotions, photographer, communication, marketing, and sales.</b></p>
    <p><b>Active since : jan 2006</b></p>
    <p><b>Shoots : 300 and counting</b></p>
    <p><b>Wil jij fotograferen voor Revelmap?</b></p>
    <p>Als je uitgaan leuk vindt, makkelijk kunt in de omgang en uitermate houdt van fotograferen, biedt Revelmap je de kans een kijkje te nemen in de wereld van de partyfotografie. Door de inzet van de fotografen is Revelmap uitgegroeid tot een van de meest toonaangevende partysites van Nederland. De betrouwbaarheid, de hoge kwaliteit van de foto's en het creeren van de beste sfeer maakt van Revelmap een van de best bezochte websites in ons vakgebied.</p>
    <p><b>Belangrijk informatie</b></p>
    <p>Fotograferen voor Revelmap is op vrijwillige basis. Je kan kiezen waar en wanneer je uitgaat en foto's maakt, maar een vaste inbreng wordt wel van je verwacht. Hoe meer je voor Revelmap doet, hoe meer ervaring je opdoet met de camera en hoe beter je wordt. Hierdoor kan je weer naar interessantere feesten en festivals. Wat je wel krijgt is gratis entree voor een evenement en soms ook andere voordelen zoals gratis drankjes... Je gaat meestal met z'n tweetjes op pad en ontmoet veel nieuwe mensen zoals DJ's en organisatoren. Hoe meer je voor Revelmap werkt hoe meer ervaring je er ook uit zal halen. De beste fotografen doen de leukste en de meest uitdagende evenementen bijvoorbeeld: Empyrean, Extremo Open Air, Sunburst weekend, Shore Dance etc.</p>
    <p><b>Voorwaarden</b></p>
    <p>- Je moet 18 jaar of ouder zijn.<br>
    - Je moet het aankunnen om hoge kwaliteit foto's te maken en professioneel gedrag vertonen.<br>
    - Je moet sociaal zijn; een open persoon zijn die ervan houdt om andere mensen te ontmoeten.<br>
    - Het is een vereiste dat je een digitale spiegelreflex-camera hebt en lichtsterke lens met vast diafragma van F2.8 en natuurlijk een externe flitser (E-TTL).<br>
    - Je bent verantwoordelijk voor je eigen vervoer om naar de evenementen te gaan waar je foto's maakt.</p>
  </div>
</section>

<section class="section planned">
  <div class="section-head head-dark">Geplande evenementen (18)<svg viewBox="0 0 22 14"><path d="M2 2l9 9 9-9" fill="none" stroke="#fff" stroke-width="4"/></svg></div>
  <ul class="section-body event-list">
    <li class="event"><div class="poster p-green" role="img" aria-label="Affiche Ritmo Plaza"><span class="date">21 augustus 2016</span></div>
      <div class="event-info"><h4>Recreatiegebied Veldmeer</h4><ul>
        <li><svg viewBox="0 0 13 13"><path d="M6.5 1a4 4 0 0 0-4 4c0 3 4 7 4 7s4-4 4-7a4 4 0 0 0-4-4z" fill="#fff"/></svg>Sportpark Westerveld, Amsterdam</li>
        <li><svg viewBox="0 0 13 13"><path d="M5 2v7.5a2 2 0 1 1-1-1.7V1h7v6.5a2 2 0 1 1-1-1.7V2z" fill="#fff"/></svg>Live / Soul / Techno / Hk</li>
        <li><svg viewBox="0 0 13 13"><circle cx="6.5" cy="6.5" r="5.5" fill="#fff"/><path d="M6.5 3v3.5h3" stroke="#1b1b1b" stroke-width="1.5" fill="none"/></svg>12:00 - 23:00 uur</li>
        <li><svg viewBox="0 0 13 13"><path d="M1 1h6l5 5-6 6-5-5z" fill="#fff"/></svg>Pre-register now for PULSEWERK Festival 2016 at - http://pulsewerkfestival.example</li></ul></div></li>
    <li class="event"><div class="poster p-teal" role="img" aria-label="Affiche Pulsewerk Festival"><span class="date">20 augustus 2016</span></div>
      <div class="event-info"><h4>Pulsewerk Festival 2016</h4><ul>
        <li><svg viewBox="0 0 13 13"><path d="M6.5 1a4 4 0 0 0-4 4c0 3 4 7 4 7s4-4 4-7a4 4 0 0 0-4-4z" fill="#fff"/></svg>Sportpark Westerveld, Amsterdam</li>
        <li><svg viewBox="0 0 13 13"><path d="M5 2v7.5a2 2 0 1 1-1-1.7V1h7v6.5a2 2 0 1 1-1-1.7V2z" fill="#fff"/></svg>Live / Soul / Techno / Hk</li>
        <li><svg viewBox="0 0 13 13"><circle cx="6.5" cy="6.5" r="5.5" fill="#fff"/><path d="M6.5 3v3.5h3" stroke="#1b1b1b" stroke-width="1.5" fill="none"/></svg>12:00 - 23:00 uur</li>
        <li><svg viewBox="0 0 13 13"><path d="M1 1h6l5 5-6 6-5-5z" fill="#fff"/></svg>Pre-register now for PULSEWERK Festival 2016 at - http://pulsewerkfestival.example</li></ul></div></li>
    <li class="event"><div class="poster p-green" role="img" aria-label="Affiche Ritmo Plaza"><span class="date">21 augustus 2016</span></div>
      <div class="event-info"><h4>Recreatiegebied Veldmeer</h4><ul>
        <li><svg viewBox="0 0 13 13"><path d="M6.5 1a4 4 0 0 0-4 4c0 3 4 7 4 7s4-4 4-7a4 4 0 0 0-4-4z" fill="#fff"/></svg>Sportpark Westerveld, Amsterdam</li>
        <li><svg viewBox="0 0 13 13"><path d="M5 2v7.5a2 2 0 1 1-1-1.7V1h7v6.5a2 2 0 1 1-1-1.7V2z" fill="#fff"/></svg>Live / Soul / Techno / Hk</li>
        <li><svg viewBox="0 0 13 13"><circle cx="6.5" cy="6.5" r="5.5" fill="#fff"/><path d="M6.5 3v3.5h3" stroke="#1b1b1b" stroke-width="1.5" fill="none"/></svg>12:00 - 23:00 uur</li>
        <li><svg viewBox="0 0 13 13"><path d="M1 1h6l5 5-6 6-5-5z" fill="#fff"/></svg>Pre-register now for PULSEWERK Festival 2016 at - http://pulsewerkfestival.example</li></ul></div></li>
    <li class="event"><div class="poster p-teal" role="img" aria-label="Affiche Pulsewerk Festival"><span class="date">20 augustus 2016</span></div>
      <div class="event-info"><h4>Pulsewerk Festival 2016</h4><ul>
        <li><svg viewBox="0 0 13 13"><path d="M6.5 1a4 4 0 0 0-4 4c0 3 4 7 4 7s4-4 4-7a4 4 0 0 0-4-4z" fill="#fff"/></svg>Sportpark Westerveld, Amsterdam</li>
        <li><svg viewBox="0 0 13 13"><path d="M5 2v7.5a2 2 0 1 1-1-1.7V1h7v6.5a2 2 0 1 1-1-1.7V2z" fill="#fff"/></svg>Live / Soul / Techno / Hk</li>
        <li><svg viewBox="0 0 13 13"><circle cx="6.5" cy="6.5" r="5.5" fill="#fff"/><path d="M6.5 3v3.5h3" stroke="#1b1b1b" stroke-width="1.5" fill="none"/></svg>12:00 - 23:00 uur</li>
        <li><svg viewBox="0 0 13 13"><path d="M1 1h6l5 5-6 6-5-5z" fill="#fff"/></svg>Pre-register now for PULSEWERK Festival 2016 at - http://pulsewerkfestival.example</li></ul></div></li>
    <li class="event"><div class="poster p-green" role="img" aria-label="Affiche Ritmo Plaza"><span class="date">21 augustus 2016</span></div>
      <div class="event-info"><h4>Recreatiegebied Veldmeer</h4><ul>
        <li><svg viewBox="0 0 13 13"><path d="M6.5 1a4 4 0 0 0-4 4c0 3 4 7 4 7s4-4 4-7a4 4 0 0 0-4-4z" fill="#fff"/></svg>Sportpark Westerveld, Amsterdam</li>
        <li><svg viewBox="0 0 13 13"><path d="M5 2v7.5a2 2 0 1 1-1-1.7V1h7v6.5a2 2 0 1 1-1-1.7V2z" fill="#fff"/></svg>Live / Soul / Techno / Hk</li>
        <li><svg viewBox="0 0 13 13"><circle cx="6.5" cy="6.5" r="5.5" fill="#fff"/><path d="M6.5 3v3.5h3" stroke="#1b1b1b" stroke-width="1.5" fill="none"/></svg>12:00 - 23:00 uur</li>
        <li><svg viewBox="0 0 13 13"><path d="M1 1h6l5 5-6 6-5-5z" fill="#fff"/></svg>Pre-register now for PULSEWERK Festival 2016 at - http://pulsewerkfestival.example</li></ul></div></li>
    <li class="event"><div class="poster p-teal" role="img" aria-label="Affiche Pulsewerk Festival"><span class="date">20 augustus 2016</span></div>
      <div class="event-info"><h4>Pulsewerk Festival 2016</h4><ul>
        <li><svg viewBox="0 0 13 13"><path d="M6.5 1a4 4 0 0 0-4 4c0 3 4 7 4 7s4-4 4-7a4 4 0 0 0-4-4z" fill="#fff"/></svg>Sportpark Westerveld, Amsterdam</li>
        <li><svg viewBox="0 0 13 13"><path d="M5 2v7.5a2 2 0 1 1-1-1.7V1h7v6.5a2 2 0 1 1-1-1.7V2z" fill="#fff"/></svg>Live / Soul / Techno / Hk</li>
        <li><svg viewBox="0 0 13 13"><circle cx="6.5" cy="6.5" r="5.5" fill="#fff"/><path d="M6.5 3v3.5h3" stroke="#1b1b1b" stroke-width="1.5" fill="none"/></svg>12:00 - 23:00 uur</li>
        <li><svg viewBox="0 0 13 13"><path d="M1 1h6l5 5-6 6-5-5z" fill="#fff"/></svg>Pre-register now for PULSEWERK Festival 2016 at - http://pulsewerkfestival.example</li></ul></div></li>
  </ul>
</section>

<section class="section past">
  <div class="section-head head-dark">Evenementen uit het verleden (250)<svg viewBox="0 0 22 14"><path d="M2 2l9 9 9-9" fill="none" stroke="#fff" stroke-width="4"/></svg></div>
  <ul class="section-body event-list">
    <li class="event"><div class="poster p-cream" role="img" aria-label="Affiche Extremo Open Air"><span class="date">20 augustus 2016</span></div>
      <div class="event-info"><h4>Recreatiegebied Veldmeer</h4><ul>
        <li><svg viewBox="0 0 13 13"><path d="M6.5 1a4 4 0 0 0-4 4c0 3 4 7 4 7s4-4 4-7a4 4 0 0 0-4-4z" fill="#fff"/></svg>Sportpark Westerveld, Amsterdam</li>
        <li><svg viewBox="0 0 13 13"><path d="M5 2v7.5a2 2 0 1 1-1-1.7V1h7v6.5a2 2 0 1 1-1-1.7V2z" fill="#fff"/></svg>Live / Soul / Techno / Hk</li>
        <li><svg viewBox="0 0 13 13"><circle cx="6.5" cy="6.5" r="5.5" fill="#fff"/><path d="M6.5 3v3.5h3" stroke="#1b1b1b" stroke-width="1.5" fill="none"/></svg>12:00 - 23:00 uur</li>
        <li><svg viewBox="0 0 13 13"><path d="M1 1h6l5 5-6 6-5-5z" fill="#fff"/></svg>Pre-register now for PULSEWERK Festival 2016 at - http://pulsewerkfestival.example</li></ul></div></li>
    <li class="event"><div class="poster p-navy" role="img" aria-label="Affiche Sunburst weekend"><span class="date">20 augustus 2016</span></div>
      <div class="event-info"><h4>Pulsewerk Festival 2016</h4><ul>
        <li><svg viewBox="0 0 13 13"><path d="M6.5 1a4 4 0 0 0-4 4c0 3 4 7 4 7s4-4 4-7a4 4 0 0 0-4-4z" fill="#fff"/></svg>Sportpark Westerveld, Amsterdam</li>
        <li><svg viewBox="0 0 13 13"><path d="M5 2v7.5a2 2 0 1 1-1-1.7V1h7v6.5a2 2 0 1 1-1-1.7V2z" fill="#fff"/></svg>Live / Soul / Techno / Hk</li>
        <li><svg viewBox="0 0 13 13"><circle cx="6.5" cy="6.5" r="5.5" fill="#fff"/><path d="M6.5 3v3.5h3" stroke="#1b1b1b" stroke-width="1.5" fill="none"/></svg>12:00 - 23:00 uur</li>
        <li><svg viewBox="0 0 13 13"><path d="M1 1h6l5 5-6 6-5-5z" fill="#fff"/></svg>Pre-register now for PULSEWERK Festival 2016 at - http://pulsewerkfestival.example</li></ul></div></li>
    <li class="event"><div class="poster p-cream" role="img" aria-label="Affiche Extremo Open Air"><span class="date">20 augustus 2016</span></div>
      <div class="event-info"><h4>Recreatiegebied Veldmeer</h4><ul>
        <li><svg viewBox="0 0 13 13"><path d="M6.5 1a4 4 0 0 0-4 4c0 3 4 7 4 7s4-4 4-7a4 4 0 0 0-4-4z" fill="#fff"/></svg>Sportpark Westerveld, Amsterdam</li>
        <li><svg viewBox="0 0 13 13"><path d="M5 2v7.5a2 2 0 1 1-1-1.7V1h7v6.5a2 2 0 1 1-1-1.7V2z" fill="#fff"/></svg>Live / Soul / Techno / Hk</li>
        <li><svg viewBox="0 0 13 13"><circle cx="6.5" cy="6.5" r="5.5" fill="#fff"/><path d="M6.5 3v3.5h3" stroke="#1b1b1b" stroke-width="1.5" fill="none"/></svg>12:00 - 23:00 uur</li>
        <li><svg viewBox="0 0 13 13"><path d="M1 1h6l5 5-6 6-5-5z" fill="#fff"/></svg>Pre-register now for PULSEWERK Festival 2016 at - http://pulsewerkfestival.example</li></ul></div></li>
    <li class="event"><div class="poster p-navy" role="img" aria-label="Affiche Sunburst weekend"><span class="date">20 augustus 2016</span></div>
      <div class="event-info"><h4>Pulsewerk Festival 2016</h4><ul>
        <li><svg viewBox="0 0 13 13"><path d="M6.5 1a4 4 0 0 0-4 4c0 3 4 7 4 7s4-4 4-7a4 4 0 0 0-4-4z" fill="#fff"/></svg>Sportpark Westerveld, Amsterdam</li>
        <li><svg viewBox="0 0 13 13"><path d="M5 2v7.5a2 2 0 1 1-1-1.7V1h7v6.5a2 2 0 1 1-1-1.7V2z" fill="#fff"/></svg>Live / Soul / Techno / Hk</li>
        <li><svg viewBox="0 0 13 13"><circle cx="6.5" cy="6.5" r="5.5" fill="#fff"/><path d="M6.5 3v3.5h3" stroke="#1b1b1b" stroke-width="1.5" fill="none"/></svg>12:00 - 23:00 uur</li>
        <li><svg viewBox="0 0 13 13"><path d="M1 1h6l5 5-6 6-5-5z" fill="#fff"/></svg>Pre-register now for PULSEWERK Festival 2016 at - http://pulsewerkfestival.example</li></ul></div></li>
    <li class="event"><div class="poster p-cream" role="img" aria-label="Affiche Extremo Open Air"><span class="date">20 augustus 2016</span></div>
      <div class="event-info"><h4>Recreatiegebied Veldmeer</h4><ul>
        <li><svg viewBox="0 0 13 13"><path d="M6.5 1a4 4 0 0 0-4 4c0 3 4 7 4 7s4-4 4-7a4 4 0 0 0-4-4z" fill="#fff"/></svg>Sportpark Westerveld, Amsterdam</li>
        <li><svg viewBox="0 0 13 13"><path d="M5 2v7.5a2 2 0 1 1-1-1.7V1h7v6.5a2 2 0 1 1-1-1.7V2z" fill="#fff"/></svg>Live / Soul / Techno / Hk</li>
        <li><svg viewBox="0 0 13 13"><circle cx="6.5" cy="6.5" r="5.5" fill="#fff"/><path d="M6.5 3v3.5h3" stroke="#1b1b1b" stroke-width="1.5" fill="none"/></svg>12:00 - 23:00 uur</li>
        <li><svg viewBox="0 0 13 13"><path d="M1 1h6l5 5-6 6-5-5z" fill="#fff"/></svg>Pre-register now for PULSEWERK Festival 2016 at - http://pulsewerkfestival.example</li></ul></div></li>
    <li class="event"><div class="poster p-navy" role="img" aria-label="Affiche Sunburst weekend"><span class="date">20 augustus 2016</span></div>
      <div class="event-info"><h4>Pulsewerk Festival 2016</h4><ul>
        <li><svg viewBox="0 0 13 13"><path d="M6.5 1a4 4 0 0 0-4 4c0 3 4 7 4 7s4-4 4-7a4 4 0 0 0-4-4z" fill="#fff"/></svg>Sportpark Westerveld, Amsterdam</li>
        <li><svg viewBox="0 0 13 13"><path d="M5 2v7.5a2 2 0 1 1-1-1.7V1h7v6.5a2 2 0 1 1-1-1.7V2z" fill="#fff"/></svg>Live / Soul / Techno / Hk</li>
        <li><svg viewBox="0 0 13 13"><circle cx="6.5" cy="6.5" r="5.5" fill="#fff"/><path d="M6.5 3v3.5h3" stroke="#1b1b1b" stroke-width="1.5" fill="none"/></svg>12:00 - 23:00 uur</li>
        <li><svg viewBox="0 0 13 13"><path d="M1 1h6l5 5-6 6-5-5z" fill="#fff"/></svg>Pre-register now for PULSEWERK Festival 2016 at - http://pulsewerkfestival.example</li></ul></div></li>
  </ul>
</section>

<section class="section photos">
  <div class="section-head head-light">Foto's (575)<svg viewBox="0 0 22 14"><path d="M2 2l9 9 9-9" fill="none" stroke="#0b0b0b" stroke-width="4"/></svg></div>
  <div class="photo-grid">
    <div class="photo big" role="img" aria-label="Feestfoto van bezoekers in oranje kleding"></div>
    <div class="photo" role="img" aria-label="Feestfoto"></div>
    <div class="photo" role="img" aria-label="Feestfoto"></div>
    <div class="photo" role="img" aria-label="Feestfoto"></div>
    <div class="photo" role="img" aria-label="Feestfoto"></div>
    <div class="photo" role="img" aria-label="Feestfoto"></div>
    <div class="photo" role="img" aria-label="Feestfoto"></div>
    <div class="photo" role="img" aria-label="Feestfoto"></div>
    <div class="photo" role="img" aria-label="Feestfoto"></div>
    <div class="photo" role="img" aria-label="Feestfoto"></div>
    <div class="photo" role="img" aria-label="Feestfoto"></div>
    <div class="photo" role="img" aria-label="Feestfoto"></div>
    <div class="photo" role="img" aria-label="Feestfoto"></div>
    <div class="photo" role="img" aria-label="Feestfoto"></div>
    <div class="photo" role="img" aria-label="Feestfoto"></div>
    <div class="photo" role="img" aria-label="Feestfoto"></div>
    <div class="photo" role="img" aria-label="Feestfoto"></div>
  </div>
</section>

<footer class="footer">
  <div class="footer-links">CONTACT<span>|</span>GEBRUIKERSVOORWAARDEN<span>|</span>PRIVACY POLICY</div>
  <div class="copyright">© 2006 - 2016 Revelmap</div>
</footer>

</body>
</html>
```